VenuMend Flyer Design - Hospitality IT, POS and Network Specialists

We need an A5 flyer (both sides) designed to be printed in full colour on thin, glossy paper. This flier will be given out in door-to-door sales.
We work from mobile vans, and we stock most hardware required for quick fix of Printers, POS, network switches, routers and Access Points, Cash Drawers, etc.
Please see our website for information: https://venumend.com.au/. Our phone number is 1300 Venum1 (1300 582 394). Please see attached our brandbook and logos.
VenuMend provides on-site technology support built specifically for hospitality venues. We help cafés, restaurants, bars, and venues keep their critical systems running — from POS and printers to networks, tablets, and ordering hardware.

We work across all major POS platforms and hardware brands, focusing on fast, practical fixes that minimise downtime and keep service moving. Unlike generic IT providers, we understand hospitality environments and the real impact technology issues have on staff and customers.

VenuMend delivers hands-on, in-venue support, clear communication, and solutions that make sense for how hospitality actually operates. We don’t sell POS software, and we don’t upsell unnecessary systems — just reliable, specialist support when your venue needs it most.

Target Market(s)

Hospitality Venues - Restaurants, Cafes, Bars, Clubs, etc

Industry/Entity Type

IT Support

Font styles to use
Sans Serif
Other font styles liked:
• Inter, Roboto, Poppins or Montserrat

Colors
0054AA
0677BA
7BADD7
CADEEF
E8F1F8

Requirements
Must have
• Information on what we do, then clear call to action - phone number, QR code with website and website itself
Nice to have
• N/A
Should not have
• N/A

```html
<!DOCTYPE html>
<html lang="en">
<head>
<meta charset="utf-8">
<title>VenuMend Flyer – Front and Back</title>
<link href="https://fonts.googleapis.com/css2?family=Montserrat:wght@400;500;600;700;800&family=Inter:wght@400;500&display=swap" rel="stylesheet">
<style>
  :root {
    --navy: #0a3a6f;
    --teal: #2bb3b0;
    --white: #ffffff;
    --stage: #d6d6d6;
    --photo-dark: #0c1a2b;
    --photo-mid: #1d3d5e;
    --photo-glow: #2e7fb0;
  }
  * { box-sizing: border-box; margin: 0; padding: 0; }
  html, body { width: 1168px; height: 1200px; overflow: hidden; }
  body {
    background: var(--stage);
    font-family: "Montserrat", sans-serif;
    position: relative;
  }
  .flyer {
    position: absolute;
    top: 232px;
    width: 520px;
    height: 736px;
    background: var(--white);
    overflow: hidden;
  }
  .flyer--back { left: 40px; }
  .flyer--front { left: 608px; }

  .hero-photo {
    position: absolute;
    top: 0; right: 0;
    width: 300px; height: 163px;
  }
  .brand {
    position: absolute;
    left: 32px; top: 44px;
  }
  .brand__name {
    font-weight: 800;
    font-size: 40px;
    letter-spacing: -1.5px;
    color: var(--navy);
    line-height: 1;
  }
  .brand__tagline {
    margin-top: 6px;
    padding-top: 4px;
    border-top: 1.5px solid var(--teal);
    font-family: "Inter", sans-serif;
    font-size: 10.5px;
    font-weight: 500;
    color: var(--navy);
    white-space: nowrap;
  }

  /* Services list */
  .services {
    position: absolute;
    left: 34px; top: 178px;
    list-style: none;
  }
  .service { margin-bottom: 17px; }
  .service__title {
    display: flex; align-items: center; gap: 4px;
    font-weight: 700;
    font-size: 21px;
    color: var(--teal);
    line-height: 1.1;
  }
  .service__icon { width: 17px; height: 17px; flex: none; }
  .service__desc {
    margin-left: 25px;
    margin-top: 2px;
    font-size: 12.5px;
    font-weight: 500;
    color: var(--navy);
    line-height: 1.3;
    max-width: 430px;
  }

  /* Front headline */
  .headline {
    position: absolute;
    left: 34px; top: 176px;
    font-weight: 800;
    text-transform: uppercase;
    color: var(--navy);
    line-height: 54px;
    font-size: 39px;
    letter-spacing: 0.3px;
  }
  .headline__brand {
    display: block;
    color: var(--teal);
    font-size: 58px;
    letter-spacing: 1px;
    line-height: 60px;
  }
  .intro {
    position: absolute;
    left: 34px; top: 470px;
    width: 450px;
    font-size: 12.5px;
    font-weight: 500;
    color: #111;
    line-height: 1.35;
  }

  /* Call to action band */
  .cta-shape { position: absolute; left: 0; top: 503px; width: 520px; height: 133px; }
  .cta-button {
    position: absolute;
    left: 45px; top: 544px;
    width: 226px; height: 54px;
    border-radius: 27px;
    background: var(--teal);
    color: var(--white);
    font-weight: 700;
    font-size: 18.5px;
    display: flex; align-items: center; justify-content: center;
  }
  .cta-phone {
    position: absolute;
    left: 296px; top: 555px;
    display: flex; align-items: center; gap: 8px;
    font-weight: 800;
    font-size: 25px;
    color: var(--teal);
  }
  .cta-phone svg { width: 21px; height: 21px; }

  /* Footer */
  .contact-bar {
    position: absolute;
    left: 0; top: 636px;
    width: 520px; height: 100px;
    background: var(--teal);
    color: var(--white);
    font-size: 13px;
    font-weight: 500;
  }
  .contact-line { position: absolute; display: flex; align-items: center; gap: 7px; white-space: nowrap; }
  .contact-line svg { width: 13px; height: 13px; }
  .contact-line--address { left: 60px; top: 13px; }
  .contact-line--email { left: 36px; top: 45px; }
  .contact-line--web { left: 290px; top: 45px; }
</style>
</head>
<body>

<svg width="0" height="0" style="position:absolute">
  <defs>
    <linearGradient id="photoTone" x1="0" y1="0" x2="1" y2="1">
      <stop offset="0" stop-color="#0c1a2b"/>
      <stop offset="0.55" stop-color="#1d3d5e"/>
      <stop offset="1" stop-color="#2e7fb0"/>
    </linearGradient>
    <symbol id="icon-phone" viewBox="0 0 20 20">
      <rect width="20" height="20" rx="4" fill="#0a3a6f"/>
      <path d="M6 4.5l2.2 0 1 3-1.4 1.1a7 7 0 0 0 3.6 3.6l1.1-1.4 3 1v2.2a1.5 1.5 0 0 1-1.6 1.5A10 10 0 0 1 4.5 6.1 1.5 1.5 0 0 1 6 4.5z" fill="#fff"/>
    </symbol>
    <symbol id="icon-pin" viewBox="0 0 14 14">
      <path d="M7 1a4 4 0 0 1 4 4c0 3-4 8-4 8S3 8 3 5a4 4 0 0 1 4-4z" fill="none" stroke="#fff" stroke-width="1.4"/>
      <circle cx="7" cy="5" r="1.4" fill="#fff"/>
    </symbol>
    <symbol id="icon-mail" viewBox="0 0 14 14">
      <rect x="1.5" y="2" width="11" height="10" rx="1.5" fill="#fff"/>
      <path d="M3.5 6h7M3.5 8.5h7" stroke="#2bb3b0" stroke-width="1.2"/>
    </symbol>
    <symbol id="icon-globe" viewBox="0 0 14 14">
      <g fill="none" stroke="#fff" stroke-width="1.2">
        <circle cx="7" cy="7" r="5.5"/><ellipse cx="7" cy="7" rx="2.4" ry="5.5"/><path d="M1.5 7h11"/>
      </g>
    </symbol>
  </defs>
</svg>

<!-- Back side: services -->
<section class="flyer flyer--back">
  <svg class="hero-photo" viewBox="0 0 300 163" role="img" aria-label="Photo of a support agent wearing a headset">
    <polygon points="0,0 300,0 300,163 93,163" fill="url(#photoTone)"/>
  </svg>
  <div class="brand">
    <div class="brand__name">VenuMend</div>
    <div class="brand__tagline">Hospitality IT, POS &amp; Network Specialists</div>
  </div>

  <ul class="services">
    <li class="service">
      <div class="service__title">
        <svg class="service__icon" viewBox="0 0 16 16"><circle cx="8" cy="8" r="5" fill="none" stroke="#2bb3b0" stroke-width="3" stroke-dasharray="2.5 1.4"/><circle cx="8" cy="8" r="2" fill="#2bb3b0"/></svg>
        POS Support</div>
      <p class="service__desc">Troubleshooting and hardware support for all POS platforms.</p>
    </li>
    <li class="service">
      <div class="service__title">
        <svg class="service__icon" viewBox="0 0 16 16"><rect x="4" y="2" width="8" height="3" fill="#2bb3b0"/><rect x="1.5" y="6" width="13" height="6" rx="1.5" fill="#2bb3b0"/><rect x="4" y="10" width="8" height="4" fill="#fff" stroke="#2bb3b0" stroke-width="1.2"/></svg>
        Printers &amp; Peripherals</div>
      <p class="service__desc">Receipt, kitchen, label printers, payment and ordering devices.</p>
    </li>
    <li class="service">
      <div class="service__title">
        <svg class="service__icon" viewBox="0 0 16 16"><g fill="none" stroke="#2bb3b0" stroke-width="1.2"><polygon points="8,1.5 14,5 14,11 8,14.5 2,11 2,5"/><path d="M8 1.5v13M2 5l12 6M14 5L2 11"/></g></svg>
        Networking Support</div>
      <p class="service__desc">Routers, switches, Wi-Fi optimisation, and internet failover.</p>
    </li>
    <li class="service">
      <div class="service__title">
        <svg class="service__icon" viewBox="0 0 16 16"><rect x="1.5" y="3" width="13" height="8.5" rx="1" fill="none" stroke="#2bb3b0" stroke-width="1.5"/><path d="M5 14h6M8 11.5V14" stroke="#2bb3b0" stroke-width="1.5"/></svg>
        Tablets &amp; Kiosks</div>
      <p class="service__desc">Set up and support for tablets, kiosks, and POS terminals</p>
    </li>
    <li class="service">
      <div class="service__title">
        <svg class="service__icon" viewBox="0 0 16 16"><g fill="none" stroke="#2bb3b0" stroke-width="1.6"><circle cx="8" cy="8" r="6"/><circle cx="8" cy="8" r="2.5"/><path d="M3.8 3.8l2.4 2.4M12.2 3.8L9.8 6.2M3.8 12.2l2.4-2.4M12.2 12.2L9.8 9.8"/></g></svg>
        On-Site Tech Support</div>
      <p class="service__desc">Hands-on troubleshooting for hospitality technology issues.</p>
    </li>
  </ul>

  <svg class="cta-shape" viewBox="0 0 520 133"><polygon points="0,0 308,0 214,133 0,133" fill="#0a3a6f"/></svg>
  <div class="cta-button">Contact Us Today!</div>
  <div class="cta-phone"><svg><use href="#icon-phone"/></svg>1300582394</div>

  <footer class="contact-bar">
    <div class="contact-line contact-line--address"><svg><use href="#icon-pin"/></svg>18 Harbour Lane, Greenhill QLD 4120, Australia</div>
    <div class="contact-line contact-line--email"><svg><use href="#icon-mail"/></svg>info@venumend.com.au</div>
    <div class="contact-line contact-line--web"><svg><use href="#icon-globe"/></svg>info@venumend.com.au</div>
  </footer>
</section>

<!-- Front side: headline -->
<section class="flyer flyer--front">
  <svg class="hero-photo" viewBox="0 0 300 163" role="img" aria-label="Photo of a support agent wearing a headset">
    <polygon points="0,0 300,0 300,163 93,163" fill="url(#photoTone)"/>
  </svg>
  <div class="brand">
    <div class="brand__name">VenuMend</div>
    <div class="brand__tagline">Hospitality IT, POS &amp; Network Specialists</div>
  </div>

  <h1 class="headline">
    <span class="headline__brand">VenuMend</span>
    Is your local<br>
    Hospitality tech<br>
    Support team,<br>
    Keeping venues
  </h1>
  <p class="intro">VenuMend provides on-site technology support built specifically for hospitality venues.</p>

  <svg class="cta-shape" viewBox="0 0 520 133"><polygon points="0,0 308,0 214,133 0,133" fill="#0a3a6f"/></svg>
  <div class="cta-button">Contact Us Today!</div>
  <div class="cta-phone"><svg><use href="#icon-phone"/></svg>1300582394</div>

  <footer class="contact-bar">
    <div class="contact-line contact-line--address"><svg><use href="#icon-pin"/></svg>18 Harbour Lane, Greenhill QLD 4120, Australia</div>
    <div class="contact-line contact-line--email"><svg><use href="#icon-mail"/></svg>info@venumend.com.au</div>
    <div class="contact-line contact-line--web"><svg><use href="#icon-globe"/></svg>info@venumend.com.au</div>
  </footer>
</section>

</body>
</html>
```